Weightloss company needs Business Card

We want a business card that is clean and professional, yet portrays that we are a friendly, innovative, and versatile program designed to fit the needs of our clients.
I would like there to be 2 sides, one side having an appointment card, and the other side containing the logo and business information. There can be decorations on both sides. The logo is attached.

Target Market(s)

Men and women 40-60

Industry/Entity Type

Business

Contact Information for Business Card

Font styles to use
Sans Serif

Requirements
Must have
• The logo, space for business information
Nice to have
• The colors in the logo
Should not have
• No pictures of people or food

```html
<!DOCTYPE html>
<html lang="en">
<head>
<meta charset="utf-8">
<title>Turnwell Weightloss – Business Card</title>
<link href="https://fonts.googleapis.com/css2?family=Open+Sans:wght@400;600;700;800&display=swap" rel="stylesheet">
<style>
  :root{
    --backdrop:#b9babd;
    --card:#ffffff;
    --brand-red:#e0173a;
    --teal-light:#63c3d0;
    --teal-dark:#53a9b5;
    --ink:#6d6d6d;
    --ink-dark:#4a4a4a;
    --label-blue:#1aa3df;
    --divider:#e0173a;
  }
  *{box-sizing:border-box;margin:0;padding:0}
  html,body{width:1200px;height:1200px;overflow:hidden}
  body{
    background:var(--backdrop);
    font-family:"Open Sans",Arial,sans-serif;
    display:flex;flex-direction:column;align-items:center;justify-content:center;gap:60px;
  }
  .card{
    position:relative;width:840px;height:480px;background:var(--card);
    box-shadow:0 6px 18px rgba(0,0,0,.18);overflow:hidden;
  }
  .brand{
    position:absolute;left:60px;display:flex;align-items:center;gap:16px;
  }
  .brand__dot{width:26px;height:26px;border-radius:50%;background:var(--brand-red);flex:none}
  .brand__name{
    font-weight:800;font-size:48px;line-height:1.02;color:var(--brand-red);letter-spacing:-.5px;
  }
  .band{position:absolute;right:0;width:330px;height:120px}
  .band svg{display:block;width:100%;height:100%}
  .band__text{position:absolute;left:64px;top:0;height:100%;display:flex;flex-direction:column;justify-content:center;color:#fff}

  /* appointment side */
  .appointment .brand{top:40px}
  .appointment .band{top:170px}
  .appointment .band__text{font-weight:600;font-size:34px;letter-spacing:1.5px}
  .slot{position:absolute;font-size:20px;font-style:italic;color:var(--ink-dark)}
  .slot__row{display:flex;align-items:baseline;gap:8px;width:250px;margin-bottom:10px}
  .slot__line{flex:1;border-bottom:2px dotted var(--ink)}

  /* contact side */
  .contact .brand{top:100px}
  .contact .band{top:130px}
  .person__name{font-weight:700;font-size:40px;line-height:1.1}
  .person__role{font-size:24px;font-weight:400}
  .details{
    position:absolute;left:60px;bottom:45px;display:flex;gap:22px;
    font-size:24px;line-height:1.35;color:var(--ink);letter-spacing:.5px;
  }
  .details__group{padding-right:22px;border-right:1px solid var(--divider)}
  .details__group:last-child{border-right:none;padding-right:0;padding-top:30px}
  .details__label{color:var(--label-blue);font-weight:700;margin-right:6px}
</style>
</head>
<body>

<section class="card appointment" aria-label="Appointment side">
  <div class="brand"><span class="brand__dot"></span><span class="brand__name">Turnwell<br>Weightloss</span></div>

  <div class="slot" style="left:60px;top:185px">
    <div class="slot__row">Date<span class="slot__line"></span></div>
    <div class="slot__row">Time<span class="slot__line"></span></div>
  </div>
  <div class="slot" style="left:150px;top:300px">
    <div class="slot__row">Date<span class="slot__line"></span></div>
    <div class="slot__row">Time<span class="slot__line"></span></div>
  </div>
  <div class="slot" style="left:470px;top:360px">
    <div class="slot__row">Date<span class="slot__line"></span></div>
    <div class="slot__row">Time<span class="slot__line"></span></div>
  </div>

  <div class="band">
    <svg viewBox="0 0 330 120" preserveAspectRatio="none" aria-hidden="true">
      <defs><linearGradient id="tealA" x1="0" y1="0" x2="0" y2="1">
        <stop offset="0" stop-color="var(--teal-light)"/><stop offset="1" stop-color="var(--teal-dark)"/>
      </linearGradient></defs>
      <path d="M36 0H330V120H0Q44 64 36 0Z" fill="url(#tealA)"/>
    </svg>
    <div class="band__text">Appointments</div>
  </div>
</section>

<section class="card contact" aria-label="Contact side">
  <div class="brand"><span class="brand__dot"></span><span class="brand__name">Turnwell<br>Weightloss</span></div>

  <div class="band">
    <svg viewBox="0 0 330 120" preserveAspectRatio="none" aria-hidden="true">
      <defs><linearGradient id="tealB" x1="0" y1="0" x2="0" y2="1">
        <stop offset="0" stop-color="var(--teal-light)"/><stop offset="1" stop-color="var(--teal-dark)"/>
      </linearGradient></defs>
      <path d="M36 0H330V120H0Q44 64 36 0Z" fill="url(#tealB)"/>
    </svg>
    <div class="band__text">
      <div class="person__name">John Doe</div>
      <div class="person__role">Director</div>
    </div>
  </div>

  <div class="details">
    <div class="details__group">
      <div><span class="details__label">T.</span>111.222.3333</div>
      <div><span class="details__label">F.</span>111.222.3333</div>
    </div>
    <div class="details__group">
      <div>www.turnwell.com</div>
      <div>info@turnwell.com</div>
    </div>
    <div class="details__group">
      <div>Dummy City</div>
      <div>Dummy Country Land</div>
    </div>
  </div>
</section>

</body>
</html>
```